The Deskwell (A new and exciting small Business support solution) Business Cards

The Deskwell Business Card Design

About us:
The Deskwell is a small business support solution, assisting businesses with any marketing, office management and human resource skills.

Objective
To be a small business lifesaver, to relieve busy professionals from mundane operations so they can focus on their businesses future through complete, reliable, efficient and effective client support. To have people say WOW what did we do before The Deskwell.

Industry/Entity Type

Small Business

Colors
0355a3
33a6d7

Requirements
Must have
• Must be similar to the look and feel of my website http://www.thedeskwell-example.com.au/

Must have:

Blue colour is 0094FF

The Logo

A Small Business Support Solution
- Human Resources
- Office Administration
- Marketing

Maribel Torvik
0462 837 105
maribeltorvik@thedeskwell-example.com.au
www.thedeskwell-example.com

```html
<!DOCTYPE html>
<html lang="en">
<head>
<meta charset="utf-8">
<title>The Deskwell – Business Cards</title>
<link href="https://fonts.googleapis.com/css2?family=Open+Sans:wght@400;600;700&display=swap" rel="stylesheet">
<style>
  :root {
    --backdrop: #e4e4e2;
    --card-blue: #5592cf;
    --card-white: #f4f4f5;
    --ink-dark: #2a2a2c;
    --ink-light: #ffffff;
    --rule-dark: #2d2d2f;
  }
  * { margin: 0; padding: 0; box-sizing: border-box; }
  html, body {
    width: 1200px; height: 1000px; overflow: hidden;
    background: var(--backdrop);
    font-family: "Open Sans", Arial, sans-serif;
  }
  .stage {
    width: 1200px; height: 1000px;
    display: flex; flex-direction: column; align-items: center; justify-content: center;
    gap: 60px;
  }
  .card {
    position: relative;
    width: 525px; height: 300px;
    background: var(--card-blue);
    overflow: hidden;
    box-shadow: 0 6px 18px rgba(0,0,0,0.12);
  }
  /* Front */
  .card-front .brand-band {
    position: absolute; left: 0; top: 0; width: 100%; height: 96px;
    background: var(--card-white);
    border-bottom: 4px solid var(--rule-dark);
  }
  .brand-name {
    position: absolute; left: 38px; bottom: 12px;
    font-size: 40px; font-weight: 400; color: var(--ink-dark);
    letter-spacing: 0.5px; line-height: 1;
  }
  .services {
    position: absolute; right: 28px; top: 116px;
    color: var(--ink-light); text-align: right;
  }
  .services .tagline {
    font-size: 13px; padding-bottom: 5px;
    border-bottom: 1px solid rgba(255,255,255,0.85);
    margin-bottom: 6px;
  }
  .services ul { list-style: none; font-size: 12.5px; line-height: 1.3; }
  .services li::before { content: "• "; }
  .contact {
    position: absolute; left: 38px; top: 168px;
    color: var(--ink-light);
  }
  .contact .person {
    font-size: 13px; font-weight: 700; letter-spacing: 0.5px;
    text-transform: uppercase;
    width: 210px; padding-bottom: 6px;
    border-bottom: 1px solid rgba(255,255,255,0.85);
    margin-bottom: 8px;
  }
  .contact p { font-size: 13px; line-height: 1.3; }
  .contact .phone { font-weight: 600; }
  /* Back */
  .card-back { display: flex; align-items: center; justify-content: center; }
  .slogan {
    font-size: 44px; font-weight: 600; line-height: 1.2;
    color: var(--ink-light); text-align: center;
  }
  .slogan .dark { color: var(--ink-dark); }
</style>
</head>
<body>
  <main class="stage">
    <section class="card card-front">
      <div class="brand-band">
        <span class="brand-name">The Deskwell.</span>
      </div>
      <div class="services">
        <p class="tagline">A Small Business Support Solution</p>
        <ul>
          <li>Human Resources</li>
          <li>Office Administration</li>
          <li>Marketing</li>
        </ul>
      </div>
      <div class="contact">
        <p class="person">Maribel Torvik</p>
        <p class="phone">0462 837 105</p>
        <p class="email">maribeltorvik@thedeskwell-example.com.au</p>
        <p class="web">www.thedeskwell-example.com</p>
      </div>
    </section>

    <section class="card card-back">
      <p class="slogan">
        <span class="dark">"</span>Calm Support<br>
        <span class="dark">For</span> Busy Teams<span class="dark">"</span>
      </p>
    </section>
  </main>
</body>
</html>
```